The bright window tour 2019

I need an improvement of my own design for a speaking tour on shame and mental health. The advertisement will be for social media. I would like someone to remove the background and do something creative and contemporary. My preference is just my head and shoulders.

Target Market(s)

Church pastors and leaders of mental health organisations

Industry/Entity Type

Mental Health

Requirements
Must have
• The same wording as original
• Delete background and replace with something that is simple but funky

```html
<!DOCTYPE html>
<html lang="en">
<head>
<meta charset="UTF-8">
<title>The Bright Window Tour 2019</title>
<link rel="stylesheet" href="https://fonts.googleapis.com/css2?family=Montserrat:wght@300;500;800&family=Russo+One&display=swap">
<style>
  :root {
    --navy-deep: #0b0c26;
    --navy: #15173f;
    --royal: #1e22b4;
    --royal-dark: #10127a;
    --white: #ffffff;
    --brand-blue: #6f8fe6;
    --accent-violet: #5b3fd6;
    --accent-cyan: #3a7bff;
    --portrait-shadow: #1a1640;
    --portrait-mid: #3e3678;
  }
  html, body {
    margin: 0;
    padding: 0;
    width: 1200px;
    height: 1200px;
    overflow: hidden;
    background: var(--navy-deep);
  }
  .poster {
    position: relative;
    width: 1200px;
    height: 1200px;
    overflow: hidden;
    background: linear-gradient(180deg, var(--navy) 0%, var(--navy-deep) 100%);
    font-family: "Montserrat", sans-serif;
  }
  .backdrop {
    position: absolute;
    left: 670px;
    top: 0;
    width: 530px;
    height: 1200px;
  }
  .title-panel {
    position: absolute;
    left: 0;
    top: 0;
    width: 670px;
    height: 1200px;
    background: linear-gradient(160deg, var(--royal) 0%, #1a1ca0 45%, var(--royal-dark) 100%);
  }
  .portrait {
    position: absolute;
    left: 480px;
    top: 160px;
    width: 720px;
    height: 1040px;
    background:
      radial-gradient(ellipse 34% 30% at 60% 28%, var(--portrait-mid) 0%, rgba(62,54,120,0.6) 55%, rgba(62,54,120,0) 100%),
      radial-gradient(ellipse 62% 40% at 58% 92%, #0c0b20 0%, #0c0b20 60%, rgba(12,11,32,0) 100%);
    -webkit-mask-image: radial-gradient(ellipse 60% 62% at 60% 58%, #000 55%, transparent 100%);
    mask-image: radial-gradient(ellipse 60% 62% at 60% 58%, #000 55%, transparent 100%);
  }
  .headline {
    position: absolute;
    left: 30px;
    top: 172px;
    width: 600px;
    margin: 0;
    text-align: center;
    color: var(--white);
    font-weight: normal;
  }
  .headline span { display: block; }
  .headline-the {
    font-family: "Montserrat", sans-serif;
    font-weight: 800;
    font-size: 206px;
    line-height: 1;
    letter-spacing: 4px;
  }
  .headline-name {
    font-family: "Montserrat", sans-serif;
    font-weight: 300;
    font-size: 92px;
    line-height: 1.14;
    letter-spacing: 2px;
  }
  .headline-name.first { margin-top: 2px; }
  .headline-year {
    font-family: "Russo One", sans-serif;
    font-size: 86px;
    line-height: 1;
    letter-spacing: 7px;
    margin-top: 28px;
  }
  .speaker-brand {
    position: absolute;
    left: 100px;
    top: 1106px;
    display: flex;
    align-items: center;
    gap: 18px;
  }
  .speaker-brand-mark {
    width: 38px;
    height: 38px;
    background: var(--brand-blue);
  }
  .speaker-brand-name {
    font-family: "Montserrat", sans-serif;
    font-weight: 500;
    font-size: 54px;
    line-height: 1;
    color: var(--brand-blue);
  }
</style>
</head>
<body>
  <main class="poster">
    <svg class="backdrop" viewBox="0 0 530 1200" aria-hidden="true">
      <defs>
        <linearGradient id="band-glow" x1="0" y1="0" x2="1" y2="1">
          <stop offset="0" stop-color="#3a7bff" stop-opacity="0.35"/>
          <stop offset="1" stop-color="#5b3fd6" stop-opacity="0.05"/>
        </linearGradient>
      </defs>
      <polygon points="120,0 250,0 530,420 530,600" fill="url(#band-glow)"/>
      <polygon points="330,0 380,0 530,230 530,305" fill="#5b3fd6" fill-opacity="0.28"/>
      <circle cx="380" cy="430" r="260" fill="none" stroke="#3a7bff" stroke-opacity="0.22" stroke-width="3"/>
      <circle cx="380" cy="430" r="320" fill="none" stroke="#5b3fd6" stroke-opacity="0.18" stroke-width="18"/>
      <circle cx="470" cy="120" r="26" fill="#3a7bff" fill-opacity="0.55"/>
      <g fill="#6f8fe6" fill-opacity="0.35">
        <circle cx="60" cy="90" r="5"/><circle cx="90" cy="90" r="5"/><circle cx="120" cy="90" r="5"/>
        <circle cx="60" cy="120" r="5"/><circle cx="90" cy="120" r="5"/><circle cx="120" cy="120" r="5"/>
      </g>
    </svg>

    <div class="title-panel"></div>
    <div class="portrait" role="img" aria-label="Head-and-shoulders portrait of the speaker in a dark v-neck shirt, lit in deep blue"></div>

    <h1 class="headline">
      <span class="headline-the">THE</span>
      <span class="headline-name first">BRIGHT</span>
      <span class="headline-name">WINDOW</span>
      <span class="headline-year">TOUR 2019</span>
    </h1>

    <div class="speaker-brand">
      <span class="speaker-brand-mark"></span>
      <span class="speaker-brand-name">dale hartley</span>
    </div>
  </main>
</body>
</html>
```